Business card design needed

We do excavation, cartage and contracting
I would quote like to have a picture of my digger as the whole back ground and the words on top. If that looks any good
Otherwise please feel free to come up with any other cool options

Cheers Marc

KLR Contracting
Excavation, Cartage, Contracting
Marcus Prewitt
www.klr-example.co.nz
021 584 067
marc@klr-example.co.nz

```html
<!DOCTYPE html>
<html lang="en">
<head>
<meta charset="utf-8">
<title>KLR Contracting – Business Card</title>
<link rel="stylesheet" href="https://fonts.googleapis.com/css2?family=Noto+Sans:wght@400;700&display=swap">
<style>
  :root {
    --brand-green: #1f5130;
    --ink: #000000;
    --paper: #ffffff;
    --edge: #1a1a1a;
  }
  * { margin: 0; padding: 0; box-sizing: border-box; }
  html, body {
    width: 1200px;
    height: 694px;
    overflow: hidden;
    background: var(--paper);
  }
  .business-card {
    position: relative;
    width: 1200px;
    height: 694px;
    background: var(--paper);
    border: 2px solid var(--edge);
    font-family: "Noto Sans", sans-serif;
    text-align: center;
  }
  .card-line {
    position: absolute;
    left: 0;
    right: 0;
    white-space: nowrap;
  }
  .brand-mark {
    top: 128px;
    font-size: 104px;
    font-weight: 700;
    line-height: 1;
    color: var(--brand-green);
    letter-spacing: 2px;
  }
  .company-name {
    top: 286px;
    font-size: 58px;
    font-weight: 700;
    line-height: 1.1;
    color: var(--brand-green);
  }
  .services {
    top: 348px;
    font-size: 29px;
    font-weight: 400;
    line-height: 1.2;
    color: var(--ink);
  }
  .person-name {
    top: 446px;
    font-size: 45px;
    font-weight: 700;
    line-height: 1.1;
    color: var(--brand-green);
  }
  .phone {
    top: 545px;
    font-size: 33px;
    line-height: 1.2;
    color: var(--ink);
  }
  .web-contacts {
    top: 591px;
    font-size: 33px;
    line-height: 1.2;
    color: var(--ink);
  }
  .web-contacts .email { margin-right: 40px; }
</style>
</head>
<body>
  <main class="business-card">
    <div class="card-line brand-mark">KLR</div>
    <h1 class="card-line company-name">KLR Contracting</h1>
    <p class="card-line services">Excavation, Cartage, Contracting</p>
    <h2 class="card-line person-name">Marcus Prewitt</h2>
    <p class="card-line phone">021 584 067</p>
    <p class="card-line web-contacts">
      <span class="email">marc@klr-example.co.nz</span><span class="website">www.klr-example.co.nz</span>
    </p>
  </main>
</body>
</html>
```